Defend science flier

Put my name and text below on one side of flier, and place other text on other side. Try to keep file about 4 by 6 or 6 by 8 inches.

Target Market(s)

Community and retailers.

Industry/Entity Type

Retail and concerned community.

Font styles to use
Serif

Requirements
Must have
• Good, eye-catching titles. Be smaller format. Not 8 by 11
Nice to have
• Black and white text. Maybe bullets etc for organizion but no decorations.
Should not have
• Any decoration

```html
<!DOCTYPE html>
<html lang="en">
<head>
<meta charset="utf-8">
<title>Defend Science Flier</title>
<link rel="stylesheet" href="https://fonts.googleapis.com/css2?family=Playfair+Display:wght@500;600&family=Bodoni+Moda:wght@400;700&display=swap">
<style>
  :root {
    --page-bg: #ffffff;
    --card-edge: #e5cfbb;
    --paper: #ece8e1;
    --paper-light: #f0ece6;
    --gold: #ad8f4b;
    --gold-dark: #8a7036;
    --band: #ab8d4c;
    --band-light: #b89a58;
    --ink: #1d1a17;
    --band-ink: #f3ead6;
  }
  * { box-sizing: border-box; margin: 0; padding: 0; }
  html, body { width: 744px; height: 1200px; overflow: hidden; background: var(--page-bg); }
  body {
    font-family: "Bodoni Moda", "Times New Roman", serif;
    color: var(--ink);
    position: relative;
  }
  .flier {
    position: absolute;
    left: 162px;
    width: 420px;
    height: 560px;
    background: var(--card-edge);
    padding: 11px;
  }
  .flier--front { top: 30px; }
  .flier--back { top: 615px; }
  .flier__frame {
    position: relative;
    width: 100%;
    height: 100%;
    border: 1px solid var(--gold);
    border-radius: 14px;
    background: linear-gradient(180deg, var(--paper-light), var(--paper));
    text-align: center;
  }
  .title {
    font-family: "Playfair Display", Georgia, serif;
    font-weight: 500;
    color: var(--gold);
    font-size: 23px;
    line-height: 1.1;
  }
  .rule {
    width: 62px;
    height: 1px;
    margin: 0 auto;
    background: linear-gradient(90deg, transparent, var(--gold), transparent);
  }
  .body-text { font-size: 11.6px; line-height: 18px; }

  /* Front */
  .front__title { padding-top: 46px; }
  .front__subtitle { font-size: 12.5px; margin-top: 6px; }
  .front .rule { margin-top: 13px; }
  .front__para { margin-top: 28px; padding: 0 22px; }
  .front__para + .front__para { margin-top: 16px; }
  .front__quote { margin-top: 16px; padding: 0 16px; }
  .front .rule--lower { margin-top: 30px; }
  .front__cta { font-size: 10px; margin-top: 16px; }
  .front__url {
    display: inline-block;
    margin-top: 6px;
    width: 247px;
    padding: 2px 0 3px;
    border-radius: 6px;
    background: var(--gold);
    color: var(--paper-light);
    font-family: "Playfair Display", Georgia, serif;
    font-weight: 600;
    font-size: 16px;
    letter-spacing: 0.6px;
  }

  /* Back */
  .back__title { padding-top: 34px; }
  .back__intro { margin-top: 8px; font-size: 12.5px; line-height: 19px; }
  .sin-list { list-style: none; margin-top: 22px; }
  .sin-list li { margin-bottom: 11px; font-size: 10px; line-height: 13px; }
  .sin-list .num {
    display: block;
    width: 9px; height: 9px;
    margin: 0 auto 4px;
    border-radius: 50%;
    background: var(--gold);
    color: var(--paper-light);
    font-size: 6.5px;
    line-height: 9px;
  }
  .sin-list b { font-weight: 700; }
  .band {
    position: absolute;
    left: -8px;
    right: -8px;
    top: 373px;
    height: 133px;
    background: linear-gradient(90deg, var(--band), var(--band-light) 50%, var(--band));
    display: flex;
    padding: 14px 14px 0;
    color: var(--band-ink);
    font-size: 7.6px;
    line-height: 13.5px;
  }
  .band::before, .band::after {
    content: "";
    position: absolute;
    bottom: -8px;
    width: 8px;
    height: 8px;
    background: var(--gold-dark);
  }
  .band::before { left: 0; border-radius: 0 0 0 6px; }
  .band::after { right: 0; border-radius: 0 0 6px 0; }
  .band__col { flex: 1; padding: 0 12px; }
  .band__col + .band__col { border-left: 1px solid rgba(243, 234, 214, 0.35); }
  .band b { font-weight: 700; }
</style>
</head>
<body>

<section class="flier flier--front front">
  <div class="flier__frame">
    <h1 class="title front__title">Martin R. Oberfeld, Ph.D.</h1>
    <p class="front__subtitle">The Newton and Einstein of psychology and History</p>
    <div class="rule"></div>
    <p class="body-text front__para">Martin’s Bio-Psych has Restructured the Liberal Arts and Sciences— from Genetics to the Fine Arts and Hollywood.</p>
    <p class="body-text front__para">Museum Catalogues, Better Nonfiction, and<br>Hollywood Films Now Use Martin’s Methods.</p>
    <p class="body-text front__para">Martin’s Biopsych is endorsed by Dr. H. Leland Crane, professor of psychiatry at Whitmore Medical School, who said:</p>
    <p class="body-text front__quote">“Modern sleep and dream research teaches us—as does Martin Oberfeld’s book Private Sin or Public Sin—that all human activities, including art and politics, are products of the human brain, and that each of us has the privilege and responsibility of using it and communicating its creations.”</p>
    <div class="rule rule--lower"></div>
    <p class="front__cta">See Martin’s homepage for more details:</p>
    <span class="front__url">www.martin-oberfeld.org</span>
  </div>
</section>

<section class="flier flier--back back">
  <div class="flier__frame">
    <h2 class="title back__title">Why Did the Culture Change?</h2>
    <p class="back__intro">During the 1960s<br>we socialized the Seven Deadly Sins. Therefore:</p>
    <ol class="sin-list">
      <li><span class="num">1</span><b>Pride</b> became <b>“Racism.”</b></li>
      <li><span class="num">2</span><b>Lust</b> became <b>“Sexism”</b> and <b>“Gender“</b> existing <b>“out there.”</b></li>
      <li><span class="num">3</span><b>Gluttony</b> became <b>“Consumer Fetishism.”</b></li>
      <li><span class="num">4</span><b>Vanity</b> became <b>“Media Images of Beauty.”</b></li>
      <li><span class="num">5</span><b>Sloth</b> became The lack of social action: <b>“Are you fighting for diversity?”</b></li>
    </ol>
    <div class="band">
      <p class="band__col">This <b>“fight for diversity”</b> inspires attacks against people like Dr. Oberfeld for asserting any reality principle about human nature.</p>
      <p class="band__col">These thugs are religious crusaders who ignore the rule of law and try to stop the progress of science. These fanatics go around and give people a <b>“tear-test”</b>—as during the Salem witch trials. Don’t let them take over.</p>
      <p class="band__col">The educational and culture elites—such as Hollywood—now reject these theological <b>“social sins.”</b> The elites are replacing theology with traditional, human-based sin.</p>
    </div>
  </div>
</section>

</body>
</html>
```